Professional, Scientific Cover Design for Nutritional / Hair Tissue Mineral Analysis (HTMA) Company

Hair tissue mineral analysis is a versatile, science-backed tool that offers a deeper understanding of your body's mineral and heavy metal profile. By evaluating long-term mineral balance and toxic exposures, HTMA provides invaluable insights that can aid in optimizing nutrition, addressing chronic health issues, and creating a personalized wellness strategy.

We have updated our logo and are in need of an updated report cover in which personalized test results are placed. We are looking for a professional and more modern look.

There are 2 small cutouts that will need to remain as shown in the picture in the brief.

Our updated logo along with color palette used will be uploaded in the brief as well as our 2 previous, outdated designs. We no longer want our address on the front cover. We also do not want images with people in them.

Thank you.

Website: www.brevuk.com

Designs look the same

• Images with people

```html
<!DOCTYPE html>
<html lang="en">
<head>
<meta charset="utf-8">
<title>Tissue Mineral Analysis – Report Covers</title>
<link rel="stylesheet" href="https://fonts.googleapis.com/css2?family=Michroma&display=swap">
<style>
  :root {
    --stage: #b1b1b1;
    --navy-deep: #04152b;
    --navy: #0a2444;
    --orange: #e8761a;
    --brand-blue: #2f5aa8;
    --white: #ffffff;
  }
  * { box-sizing: border-box; margin: 0; padding: 0; }
  html, body {
    width: 1200px; height: 800px; overflow: hidden;
    background: var(--stage);
    font-family: "Michroma", sans-serif;
  }
  .cover {
    position: absolute;
    top: 86px;
    width: 482px; height: 624px;
    overflow: hidden;
    background: linear-gradient(180deg, var(--navy-deep), var(--navy) 55%, var(--navy-deep));
  }
  .cover--dark { left: 78px; }
  .cover--light { left: 622px; }
  .molecule-art {
    position: absolute; right: 0; top: 0;
    width: 260px; height: 470px;
    background: linear-gradient(200deg, rgba(232,118,26,.55) 0%, rgba(200,100,40,.35) 45%, rgba(43,120,176,.3) 80%, rgba(43,120,176,0) 100%);
    -webkit-mask-image: linear-gradient(90deg, transparent 0%, #000 45%);
            mask-image: linear-gradient(90deg, transparent 0%, #000 45%);
  }
  .cover--light .fade {
    position: absolute; left: 0; right: 0; top: 310px; bottom: 0;
    background: linear-gradient(180deg, rgba(255,255,255,0) 0%, rgba(255,255,255,.85) 50%, var(--white) 72%);
  }
  .title {
    position: absolute;
    color: var(--white);
    font-size: 20px;
    font-weight: 400;
    line-height: 25px;
    letter-spacing: 11px;
    font-style: italic;
    text-transform: uppercase;
  }
  .cover--dark .title { left: 52px; top: 354px; }
  .cover--light .title { left: 54px; top: 340px; }
  .brand {
    position: absolute; left: 52px;
    display: flex; align-items: center; gap: 8px;
    color: var(--brand-blue);
    font-size: 11.5px; letter-spacing: .5px;
  }
  .brand__dot {
    width: 14px; height: 14px; border-radius: 50%;
    background: var(--brand-blue);
  }
  .cover--dark .brand { top: 538px; }
  .cover--light .brand { top: 536px; left: 54px; }
  .web {
    position: absolute; left: 52px;
    color: var(--orange);
    font-size: 10px;
  }
  .cover--dark .web { top: 568px; letter-spacing: 11px; }
  .cover--light .web { top: 38px; left: 54px; letter-spacing: 4px; }
</style>
</head>
<body>
  <section class="cover cover--dark">
    <div class="molecule-art" role="img" aria-label="Glowing orange and blue molecular structure illustration"></div>
    <h1 class="title">Tissue<br>Mineral<br>Analysis</h1>
    <div class="brand"><span class="brand__dot"></span><span>BREVUK ANALYTICAL LABS</span></div>
    <p class="web">www.brevuk.com</p>
  </section>

  <section class="cover cover--light">
    <div class="molecule-art" role="img" aria-label="Glowing orange and blue molecular structure illustration"></div>
    <div class="fade"></div>
    <p class="web">www.brevuk.com</p>
    <h1 class="title">Tissue<br>Mineral<br>Analysis</h1>
    <div class="brand"><span class="brand__dot"></span><span>BREVUK ANALYTICAL LABS</span></div>
  </section>
</body>
</html>
```